Copperfield Roofing Co. business card design

I am a Roofing contractor in Texas. The name of my company is Copperfield Roofing Co. I also offer a few other services (Christmas light installation, gutters, fencing, pressure washing). However my main gig is roofing. Storm restoration and knowledge of the insurance claim process is my specialty.

My colors are black, red and white. I’d like something pretty simple and clean. Modern looking but with a splash of this red tartan pattern.

I have another version of my logo being edited at the moment where the little top part of the F in roofing that’s currently tartan will be changed to just solid red to make it more visible. So if that’s something you can change in your mock up great. But I can provide the full version once the contest is complete

Target Market(s)

Homeowners

Industry/Entity Type

Roofing

Contact Information for Business Card

Derek Pruitt. 682-555-0193. www.copperfield roofing.co Derek@copperfieldroofing.co

Colors
EB3D1F
EC4F4E
F09395
F8D3D4
FCEDEE

Requirements
Nice to have
• Maybe instead of a business address. I could say serving all DFW Texas or something like that. And maybe add a line somewhere saying deductible assistance? Just a thought

```html
<!DOCTYPE html>
<html lang="en">
<head>
<meta charset="utf-8">
<title>Copperfield Roofing Co. – Business Card</title>
<link rel="stylesheet" href="https://fonts.googleapis.com/css2?family=Montserrat:wght@400;500;600;700;800&display=swap">
<style>
  :root {
    --stage: #e8e5e0;
    --card-white: #ffffff;
    --card-black: #000000;
    --brand-red: #d8141b;
    --ink: #1a1a1a;
    --muted: #444444;
    --rule: #9a1116;
    --text-white: #ffffff;
  }
  * { margin: 0; padding: 0; box-sizing: border-box; }
  html, body {
    width: 900px; height: 1200px; overflow: hidden;
    background: var(--stage);
    font-family: "Montserrat", sans-serif;
  }
  .canvas { position: relative; width: 900px; height: 1200px; }

  .card {
    position: absolute; left: 80px; width: 742px; height: 440px;
    border-radius: 34px; overflow: hidden;
    box-shadow: 0 6px 16px rgba(0,0,0,0.25);
  }
  .card--front { top: 132px; background: var(--card-white); }
  .card--back  { top: 640px; background: var(--card-black); }

  .brand { position: absolute; left: 0; width: 100%; text-align: center; }
  .brand__mark {
    display: block; margin: 0 auto; border-radius: 50%;
    background: var(--brand-red);
  }
  .brand__name {
    font-weight: 800; line-height: 1.05; letter-spacing: 1px; text-transform: uppercase;
  }
  .brand__name span { display: block; }
  .brand__name .line-main { font-size: 38px; }
  .brand__name .line-sub { font-size: 24px; letter-spacing: 2px; }

  .card--front .brand { top: 40px; }
  .card--front .brand__mark { width: 136px; height: 136px; }
  .card--front .brand__name { margin-top: 22px; color: var(--brand-red); }

  .card--back .brand { top: 70px; }
  .card--back .brand__mark {
    width: 188px; height: 188px; border: 6px solid var(--text-white);
  }
  .card--back .brand__name { margin-top: 26px; color: var(--text-white); }
  .card--back .brand__name .line-main { font-size: 48px; }
  .card--back .brand__name .line-sub { font-size: 32px; }

  .person {
    position: absolute; right: 420px; top: 306px; text-align: right;
  }
  .person__name { font-size: 26px; font-weight: 600; color: var(--brand-red); }
  .person__role { font-size: 16px; color: var(--muted); margin-top: 2px; }

  .divider {
    position: absolute; left: 346px; top: 306px; width: 2px; height: 58px;
    background: var(--rule);
  }

  .contacts {
    position: absolute; left: 372px; top: 304px; list-style: none;
    font-size: 16px; color: var(--ink);
  }
  .contacts li { display: flex; align-items: center; height: 21px; }
  .contacts svg { width: 13px; height: 13px; margin-right: 15px; fill: var(--brand-red); flex: none; }

  .address-band {
    position: absolute; left: 0; top: 384px; width: 100%; height: 28px;
    background: var(--brand-red); color: var(--text-white);
    font-size: 16px; text-align: center; line-height: 28px;
  }
</style>
</head>
<body>
<main class="canvas">

  <section class="card card--front" aria-label="Business card front">
    <div class="brand">
      <span class="brand__mark" aria-hidden="true"></span>
      <h1 class="brand__name"><span class="line-main">Copperfield</span><span class="line-sub">Roofing Co.</span></h1>
    </div>

    <div class="person">
      <p class="person__name">Derek Pruitt</p>
      <p class="person__role">Owner</p>
    </div>
    <div class="divider"></div>

    <ul class="contacts">
      <li>
        <svg viewBox="0 0 16 16" aria-hidden="true"><path d="M1 5c0-2 3-3 7-3s7 1 7 3v2h-4V5.5H5V7H1z M3 8h10l1 6H2z M8 9.5a2 2 0 1 0 0.01 0z"/></svg>
        682-555-0193
      </li>
      <li>
        <svg viewBox="0 0 16 16" aria-hidden="true"><path d="M1 3h14v1.5L8 9 1 4.5z M1 6.3l7 4.5 7-4.5V13H1z"/></svg>
        Derek@copperfieldroofing.co
      </li>
      <li>
        <svg viewBox="0 0 16 16" aria-hidden="true"><circle cx="8" cy="8" r="7"/><path d="M4 5c2 0 2 2 4 2s1 3-1 3-1 3-3 2z M10 3c1 1 3 2 2 4-1 0-2-2-2-4z" fill="#ffffff"/></svg>
        www.copperfieldroofing.co
      </li>
    </ul>

    <div class="address-band">2418 Cedar Ridge Dr, Fort Worth TX</div>
  </section>

  <section class="card card--back" aria-label="Business card back">
    <div class="brand">
      <span class="brand__mark" aria-hidden="true"></span>
      <h2 class="brand__name"><span class="line-main">Copperfield</span><span class="line-sub">Roofing Co.</span></h2>
    </div>
  </section>

</main>
</body>
</html>
```